R&T Architects - business card and stationary

Aloha,

We have a simple text logo, we need it incorporated into a business card and also stationary design (letterhead) if possible.

Please check out our website, rtamaui-studio.example for a little more about us. The logo we would like to use is in the upper left corner of the website. It is a simple colored logo based on the Klavica font. We are open to new logo's as well, but we want simple.

Thanks

```html
<!DOCTYPE html>
<html lang="en">
<head>
<meta charset="utf-8">
<title>R&amp;T Architects – Business Card</title>
<link rel="stylesheet" href="https://fonts.googleapis.com/css2?family=Questrial&family=Arimo:wght@400&display=swap">
<style>
  :root {
    --olive-dark: #6b5a32;
    --leaf-green: #8fb034;
    --sand: #c6b48e;
    --paper: #ffffff;
    --ink: #4a4030;
    --rule: #c6b48e;
    --stage: #ffffff;
  }
  * { box-sizing: border-box; margin: 0; padding: 0; }
  html, body { width: 1200px; height: 900px; overflow: hidden; background: var(--stage); }
  .canvas { position: relative; width: 1200px; height: 900px; }

  .wordmark {
    position: absolute; left: 696px; top: 120px;
    display: flex; align-items: center; gap: 14px;
    font-family: "Questrial", sans-serif; font-size: 58px; color: var(--olive-dark);
    letter-spacing: 1px;
  }
  .wordmark .dot { width: 18px; height: 18px; border-radius: 50%; background: var(--leaf-green); }

  .card { position: absolute; width: 330px; height: 540px; }
  .card--front { left: 60px; top: 200px; background: var(--sand); }
  .card--front .monogram {
    position: absolute; left: 0; right: 0; top: 240px; text-align: center;
    font-family: "Questrial", sans-serif; font-size: 88px; color: var(--olive-dark); letter-spacing: 4px;
  }

  .card--back {
    left: 440px; top: 250px; background: var(--paper);
    box-shadow: 0 0 0 1px #e4e0d6, 0 6px 18px rgba(0,0,0,0.08);
    font-family: "Arimo", sans-serif; color: var(--ink);
  }
  .person { position: absolute; top: 28px; left: 0; right: 0; text-align: center; font-family: "Arimo", sans-serif; }
  .person .name { font-size: 20px; color: var(--leaf-green); }
  .person .role { font-size: 17px; color: var(--sand); }
  .contact { position: absolute; top: 128px; left: 0; right: 0; text-align: center; }
  .contact .email { font-size: 16px; color: var(--ink); }
  .contact .phone { margin-top: 18px; font-size: 21px; color: var(--sand); letter-spacing: 1px; }
  .brand { position: absolute; top: 268px; left: 0; right: 0; text-align: center; }
  .brand .name { font-family: "Questrial", sans-serif; font-size: 34px; color: var(--olive-dark); }
  .brand .tagline { margin: 12px auto 0; width: 290px; font-size: 11px; line-height: 1.4; color: var(--ink); }
  .brand .site { margin-top: 16px; font-size: 15px; color: var(--sand); }
  .addresses { position: absolute; top: 432px; left: 22px; right: 22px; height: 90px; font-size: 10.5px; line-height: 2.1; }
  .addresses .office { position: absolute; left: 0; top: 0; }
  .addresses .mailing { position: absolute; right: 0; top: 14px; text-align: right; }
  .addresses .divider {
    position: absolute; left: 50%; top: -12px; height: 100px; border-left: 2px dashed var(--rule);
  }
</style>
</head>
<body>
<main class="canvas">
  <div class="wordmark"><span class="dot"></span><span>R&amp;T Architects</span></div>

  <section class="card card--front" aria-label="Business card front">
    <div class="monogram">R&amp;T</div>
  </section>

  <section class="card card--back" aria-label="Business card back">
    <div class="person">
      <p class="name">Keoni Lindqvist</p>
      <p class="role">Architect</p>
    </div>
    <div class="contact">
      <p class="email">keoni@rtamaui-studio.example</p>
      <p class="phone">808.555.0142</p>
    </div>
    <div class="brand">
      <p class="name">R&amp;T Architects</p>
      <p class="tagline">Full service architecture firm with expertise in environmentally responsible, net zero energy design.</p>
      <p class="site">www.rtamaui-studio.example</p>
    </div>
    <div class="addresses">
      <div class="office">office:<br>41-880 Malana Road<br>Waimea, Hawaii 96799</div>
      <div class="divider"></div>
      <div class="mailing">mailing:<br>41-880 Puakea Place<br>Waimea, Hawaii 96799</div>
    </div>
  </section>
</main>
</body>
</html>
```